Inventory - Current and Future

I'm looking for a responsive web design for an application that will show multiple items in an inventory with pictures (of different sizes), users need to log in, add "items" into the inventory in a fun way, including uploading images and providing linked URLs.
A walkthrough of how we anticipate the user working with the software is included in the attachment.
When specifying an item, there are a number of pieces of information to capture (make/model/price/url) so allow for data entry of fields.
User should be able to scroll through a list with groups (imagine an inventory of dresses, or shoes, or appliances - like a story) - as well as "find" items (so search results are needed). They should also be able to "share" items. So pages are required as a minimum for the following:
Welcome screen / Login (could be part of key UI)
Search Results / List of items grouped by category (with images)
Individual Detail Item (with image and update information) - multiple images (with update button)
Share screen showing item with multiple people available to be "selected" to share
Target Market(s)
Consumer / (could be used for either Business/Home)
Industry/Entity Type
Small Business
Coding
Coded - Design and coding required
Number of Pages Required
3 page
Requirements
Must have
- Responsive design - view on any device nicely
- Welcome screen / Login
- List of items grouped by category (with images) / Search results
- Individual Detail Item (with image and update information) - multiple images (with update button)
- Share screen showing item with multiple people available to be "selected"
Nice to have
- Avatars / Logos
- Multiple item update
- Expand / Collapse on showing details
- Mobile support (style) for uploading images - imagine someone taking a picture and uploading, etc
Should not have
- Too business - the goal is to get enthusiastic reception and fun to gain acceptance

```html
<!DOCTYPE html>
<html lang="en">
<head>
<meta charset="utf-8">
<title>My Inventory – Item List</title>
<link rel="stylesheet" href="https://fonts.googleapis.com/css2?family=Figtree:wght@400;500;600;700&family=Lato:wght@400&display=swap">
<style>
:root{
  --orange:#f37338;
  --ink:#2f2f2f;
  --dark:#2c2c2c;
  --row-light:#f3f3f3;
  --row-dark:#e9e9e9;
  --line:#ffffff;
  --field:#e4e4e4;
}
*{box-sizing:border-box;margin:0;padding:0}
html,body{width:1200px;height:831px;overflow:hidden;background:#fff}
body{font-family:"Figtree",sans-serif;color:var(--ink);position:relative}
.topbar{height:52px;background:var(--orange);display:flex;align-items:center;justify-content:space-between;padding:0 22px 0 29px;color:#fff}
.brand{font-size:25px;font-weight:700;letter-spacing:.5px}
.logout{display:flex;align-items:center;gap:7px;font-size:17px;font-weight:600;letter-spacing:.5px}
.profile{position:absolute;left:19px;top:69px;display:flex;align-items:center;gap:8px}
.avatar{width:48px;height:48px;border-radius:50%;background:linear-gradient(135deg,#b8a48f,#6f6257);border:2px solid #ddd}
.user-name{font-size:25px;font-weight:500;color:#333}
.toolbar{position:absolute;top:85px;left:0;width:1200px;font-size:13.5px;color:#444}
.tool{position:absolute;display:flex;align-items:center;gap:7px;white-space:nowrap}
.category{position:absolute;top:174px;left:24px;display:flex;align-items:center;gap:12px;font-size:15.5px;color:#333}
.select{width:132px;height:27px;border:1px solid #ccc;display:flex;align-items:center;justify-content:space-between;padding:2px 2px 2px 9px;font-size:12px;color:#555}
.select .btn{width:30px;height:21px;background:var(--orange);display:flex;align-items:center;justify-content:center}
.app-label{position:absolute;top:174px;right:22px;font-size:16px;color:#333;line-height:22px}
.grid{position:absolute;left:27px;top:235px;width:1147px;border-collapse:collapse;table-layout:fixed}
.grid th{background:var(--orange);color:#fff;font-weight:600;font-size:13.5px;text-align:left;padding:0 11px;height:44px;border-right:1px solid rgba(255,255,255,.35);white-space:nowrap}
.grid .filters td{background:var(--dark);height:45px;padding:0 8px;border-right:1px solid #444}
.filter{height:27px;background:var(--field);display:flex;align-items:center;justify-content:space-between;padding:2px 2px 2px 7px;font-size:11.5px;color:#333}
.filter .btn{width:26px;height:23px;background:var(--orange);display:flex;align-items:center;justify-content:center}
.grid .item td{height:80px;font-size:14px;color:#333;padding:0 11px;border-right:1px solid var(--line)}
.grid .item:nth-child(even) td{background:var(--row-light)}
.grid .item:nth-child(odd) td{background:var(--row-dark)}
.grid .item td.model-active{color:var(--orange)}
.check{width:13px;height:13px;border:1px solid #c8c8c8;background:#fff;display:block;margin:0 auto}
th .check{width:15px;height:15px;border:none}
.thumb{width:116px;height:75px;background:#fff;margin:0 auto;display:flex;align-items:center;justify-content:center}
.thumb span{display:block;width:80px;height:56px;border-radius:4px}
.grid .item td.dates{text-align:center;font-size:13px;line-height:16.5px}
.grid .item td.price{font-weight:700;font-size:15px;text-align:center}
.grid .item td.action-cell{padding:0}
.actions{display:flex;gap:10px;padding-left:7px;font-size:13px;color:#444}
.actions div{display:flex;flex-direction:column;align-items:center;gap:3px}
.scroll{position:absolute;left:1165px;top:324px;width:8px;height:400px;background:#ddd}
.scroll i{position:absolute;left:1px;top:9px;width:6px;height:96px;background:var(--orange);border-radius:3px}
.pager{position:absolute;top:736px;left:28px;display:flex;align-items:center;gap:10px;font-size:13px;color:#444}
.pager .ring{width:22px;height:22px;border:1px solid #555;border-radius:50%;display:flex;align-items:center;justify-content:center;font-size:11px}
.pager .num{width:12px;text-align:center}
.footer{position:absolute;top:793px;width:1200px;text-align:center;font-family:"Lato",sans-serif;font-size:13px;color:#444}
</style>
</head>
<body>
<header class="topbar">
  <div class="brand">MY INVENTORY</div>
  <div class="logout">
    <svg width="17" height="17" viewBox="0 0 20 20" fill="none" stroke="#fff" stroke-width="2.6" stroke-linecap="round"><path d="M6 4.5a7 7 0 1 0 8 0"/><path d="M10 2v8"/></svg>
    LOGOUT
  </div>
</header>

<div class="profile">
  <div class="avatar" role="img" aria-label="User profile photo"></div>
  <div class="user-name">Daniel Morrow</div>
</div>

<nav class="toolbar">
  <div class="tool" style="left:549px">
    <svg width="20" height="18" viewBox="0 0 20 18" fill="#333"><rect x="5" y="0" width="10" height="5"/><rect x="0" y="5" width="20" height="9" rx="2"/><rect x="5" y="11" width="10" height="7" fill="#fff" stroke="#333" stroke-width="1.5"/></svg>
    Print
    <svg width="10" height="6" viewBox="0 0 10 6" fill="#333" style="margin-left:4px"><path d="M0 0h10L5 6z"/></svg>
  </div>
  <div class="tool" style="left:652px">
    <svg width="18" height="16" viewBox="0 0 18 16" fill="#333"><rect y="0" width="18" height="4"/><rect y="6" width="18" height="4"/><rect y="12" width="18" height="4"/></svg>
    Select Columns
  </div>
  <div class="tool" style="left:814px">
    <svg width="18" height="16" viewBox="0 0 18 16" fill="#333"><rect width="4" height="4"/><rect x="6" width="12" height="4"/><rect y="6" width="4" height="4"/><rect x="6" y="6" width="12" height="4"/><rect y="12" width="4" height="4"/><rect x="6" y="12" width="12" height="4"/></svg>
    List View
  </div>
  <div class="tool" style="left:931px">
    <svg width="18" height="17" viewBox="0 0 18 17" fill="none" stroke="#333" stroke-width="1.8"><rect x="4" y="1" width="13" height="12"/><path d="M1 4v12h13"/><path d="M6 11l3-4 2 3 2-2 3 3" stroke-width="1.4"/></svg>
    Gallery View
  </div>
  <div class="tool" style="left:1071px">
    <svg width="18" height="16" viewBox="0 0 18 16"><rect x="1" y="1" width="16" height="14" fill="none" stroke="#333" stroke-width="2"/><path d="M2 14l5-6 4 4 2-2 4 4z" fill="#333"/><circle cx="12" cy="5" r="1.6" fill="#333"/></svg>
    Images View
  </div>
</nav>

<div class="category">
  <span>Category Selection :</span>
  <div class="select">Office Item
    <span class="btn"><svg width="12" height="7" viewBox="0 0 12 7" fill="#fff"><path d="M0 0h12L6 7z"/></svg></span>
  </div>
</div>
<div class="app-label">Inventory Management Application</div>

<table class="grid">
  <colgroup>
    <col style="width:45px"><col style="width:130px"><col style="width:161px"><col style="width:144px"><col style="width:157px"><col style="width:88px"><col style="width:116px"><col style="width:84px"><col style="width:132px"><col style="width:90px">
  </colgroup>
  <thead>
    <tr>
      <th><span class="check"></span></th>
      <th>Model</th><th>Description</th><th>Image</th><th>Start Date / End date</th><th>Make</th><th>Serial Number</th><th>Quantity</th><th>Purchased Price</th><th>Action</th>
    </tr>
  </thead>
  <tbody>
    <tr class="filters">
      <td></td>
      <td><div class="filter">Select model<span class="btn"><svg width="12" height="13" viewBox="0 0 12 13" fill="#fff"><path d="M0 0h12L7.5 6v7L4.5 11V6z"/></svg></span></div></td>
      <td><div class="filter">Quisque et arcu<span class="btn"><svg width="12" height="13" viewBox="0 0 12 13" fill="#fff"><path d="M0 0h12L7.5 6v7L4.5 11V6z"/></svg></span></div></td>
      <td></td>
      <td><div class="filter">30/12/2016<span class="btn"><svg width="12" height="13" viewBox="0 0 12 13" fill="#fff"><path d="M0 0h12L7.5 6v7L4.5 11V6z"/></svg></span></div></td>
      <td></td><td></td><td></td>
      <td><div class="filter">$10 - $1500<span class="btn"><svg width="12" height="13" viewBox="0 0 12 13" fill="#fff"><path d="M0 0h12L7.5 6v7L4.5 11V6z"/></svg></span></div></td>
      <td></td>
    </tr>
    <tr class="item">
      <td><span class="check"><svg width="11" height="11" viewBox="0 0 11 11" fill="none" stroke="#f37338" stroke-width="1.6"><path d="M2 5.5l2.5 2.5L9 2.5"/></svg></span></td>
      <td class="model-active">ITM-1</td><td>Donec Non Gravida</td>
      <td><div class="thumb"><span role="img" aria-label="Desktop computer with monitor" style="background:linear-gradient(135deg,#c9c9cf,#8a6fa8)"></span></div></td>
      <td class="dates">30/12/2016<br>To<br>05/12/2016</td><td>Eleifend</td><td>#CA0012</td><td>10</td><td class="price">$ 1200</td>
      <td class="action-cell"><div class="actions"><div><svg width="14" height="14" viewBox="0 0 14 14" fill="#f37338"><circle cx="11" cy="3" r="2.3"/><circle cx="3" cy="7" r="2.3"/><circle cx="11" cy="11" r="2.3"/><path d="M3 7l8-4M3 7l8 4" stroke="#f37338" stroke-width="1.4"/></svg>Share</div><div><svg width="14" height="14" viewBox="0 0 14 14" fill="none" stroke="#f37338" stroke-width="1.6"><path d="M7 2H2v10h10V7"/><path d="M6 8l1-3 5-4 2 2-5 4z"/></svg>Edit</div></div></td>
    </tr>
    <tr class="item">
      <td><span class="check"></span></td>
      <td>ITM-2</td><td>Donec Non Gravida</td>
      <td><div class="thumb"><span role="img" aria-label="Desktop monitor with keyboard" style="background:linear-gradient(135deg,#2a7fd0,#1b1b1b)"></span></div></td>
      <td class="dates">20/12/2016<br>To<br>26/12/2016</td><td>Eleifend</td><td>#CA0014</td><td>5</td><td class="price">$ 40</td>
      <td class="action-cell"><div class="actions"><div><svg width="14" height="14" viewBox="0 0 14 14" fill="#f37338"><circle cx="11" cy="3" r="2.3"/><circle cx="3" cy="7" r="2.3"/><circle cx="11" cy="11" r="2.3"/><path d="M3 7l8-4M3 7l8 4" stroke="#f37338" stroke-width="1.4"/></svg>Share</div><div><svg width="14" height="14" viewBox="0 0 14 14" fill="none" stroke="#f37338" stroke-width="1.6"><path d="M7 2H2v10h10V7"/><path d="M6 8l1-3 5-4 2 2-5 4z"/></svg>Edit</div></div></td>
    </tr>
    <tr class="item">
      <td><span class="check"></span></td>
      <td>ITM-3</td><td>Donec Non Gravida</td>
      <td><div class="thumb"><span role="img" aria-label="Row of colourful ring binders" style="background:linear-gradient(90deg,#e0a030,#2a5ba8,#2f8a4a,#c83a3a)"></span></div></td>
      <td class="dates">20/12/2016<br>To<br>26/12/2016</td><td>Eleifend</td><td>#SS0015</td><td>2</td><td class="price">$ 10</td>
      <td class="action-cell"><div class="actions"><div><svg width="14" height="14" viewBox="0 0 14 14" fill="#f37338"><circle cx="11" cy="3" r="2.3"/><circle cx="3" cy="7" r="2.3"/><circle cx="11" cy="11" r="2.3"/><path d="M3 7l8-4M3 7l8 4" stroke="#f37338" stroke-width="1.4"/></svg>Share</div><div><svg width="14" height="14" viewBox="0 0 14 14" fill="none" stroke="#f37338" stroke-width="1.6"><path d="M7 2H2v10h10V7"/><path d="M6 8l1-3 5-4 2 2-5 4z"/></svg>Edit</div></div></td>
    </tr>
    <tr class="item">
      <td><span class="check"></span></td>
      <td>ITM-4</td><td>Donec Non Gravida</td>
      <td><div class="thumb"><span role="img" aria-label="Desk organiser with notepad" style="background:linear-gradient(135deg,#5a4aa8,#2e2466)"></span></div></td>
      <td class="dates">20/12/2016<br>To<br>26/12/2016</td><td>Eleifend</td><td>#SA0018</td><td>5</td><td class="price">$ 20</td>
      <td class="action-cell"><div class="actions"><div><svg width="14" height="14" viewBox="0 0 14 14" fill="#f37338"><circle cx="11" cy="3" r="2.3"/><circle cx="3" cy="7" r="2.3"/><circle cx="11" cy="11" r="2.3"/><path d="M3 7l8-4M3 7l8 4" stroke="#f37338" stroke-width="1.4"/></svg>Share</div><div><svg width="14" height="14" viewBox="0 0 14 14" fill="none" stroke="#f37338" stroke-width="1.6"><path d="M7 2H2v10h10V7"/><path d="M6 8l1-3 5-4 2 2-5 4z"/></svg>Edit</div></div></td>
    </tr>
    <tr class="item">
      <td><span class="check"></span></td>
      <td>ITM-5</td><td>Donec Non Gravida</td>
      <td><div class="thumb"><span role="img" aria-label="Black inkjet printer with photo print" style="background:linear-gradient(180deg,#1e1e1e,#3a6fa0)"></span></div></td>
      <td class="dates">20/12/2016<br>To<br>26/12/2016</td><td>Eleifend</td><td>#SS0016</td><td>1</td><td class="price">$ 160</td>
      <td class="action-cell"><div class="actions"><div><svg width="14" height="14" viewBox="0 0 14 14" fill="#f37338"><circle cx="11" cy="3" r="2.3"/><circle cx="3" cy="7" r="2.3"/><circle cx="11" cy="11" r="2.3"/><path d="M3 7l8-4M3 7l8 4" stroke="#f37338" stroke-width="1.4"/></svg>Share</div><div><svg width="14" height="14" viewBox="0 0 14 14" fill="none" stroke="#f37338" stroke-width="1.6"><path d="M7 2H2v10h10V7"/><path d="M6 8l1-3 5-4 2 2-5 4z"/></svg>Edit</div></div></td>
    </tr>
  </tbody>
</table>
<div class="scroll"><i></i></div>

<nav class="pager">
  <span class="ring">&laquo;</span>
  <span class="ring" style="font-size:13px">1</span>
  <span class="num">2</span><span class="num">3</span><span class="num">4</span>
  <span class="ring">&raquo;</span>
</nav>

<footer class="footer">Copyright © 2017 My Inventory_Web App.&nbsp; All Rights Reserved.</footer>
</body>
</html>
```